Webdesign für SEO-Agentur
Zielgruppe
Wir bieten kleinen und mittelständischen Unternehmen Suchmaschinenoptimierung zum fairen Preis mit Erfolgsgarantie an. Unsere Zielgruppe sind Unternehmer die bisher wenig oder gar keine Erfahrungen mit SEO hatten. Wir möchten Unternehmen dabei helfen ihren digitalen Auftritt sowie dessen Sichtbarkeit zu verbessern um neue Kunden zu finden.
Aufgabenstellung
- seriöses und modernes Design bei gleichzeitig ansprechender Gestaltung
- passend zum Namen möchten wir, dass die Website einen leichten wissenschaftlichen/chemischen Touch erhält. Beachten Sie daher unsere Skizze zur Schritt für Schritt Darstellung. Weitere kleine Hinweise in Richtung Chemie oder Wissenschaft können und sollen eingebaut werden.
- vorerst nur Landing-Page, daher keine Navigation nötig. Wir erwarten eine vollständige Desktop sowie Mobilversion in Ihrem Design.
- Einhaltung der vorgegebenen Inhalte
- keine langweiligen Standard-Designs, auch besondere Seiten können seriös sein
- Header ist für Portrait der Mitarbeiter reserviert und benötigt daher eine gewisse freie Fläche

```html
<!DOCTYPE html>
<html lang="de">
<head>
<meta charset="utf-8">
<title>Vexalin – SEO-Agentur</title>
<link href="https://fonts.googleapis.com/css2?family=Lato:wght@300;400;700&display=swap" rel="stylesheet">
<style>
  :root {
    --navy: #0a3764;
    --red: #e8174a;
    --bg: #f7f7f7;
    --text: #6b6b6b;
    --muted: #9a9a9a;
    --panel: #e2e2e2;
    --white: #ffffff;
  }
  * { box-sizing: border-box; margin: 0; padding: 0; }
  html, body { width: 1200px; height: 3575px; overflow: hidden; }
  body { position: relative; background: var(--bg); font-family: 'Lato', sans-serif; color: var(--text); }
  .abs { position: absolute; }
  .shapes { position: absolute; left: 0; top: 0; width: 1200px; height: 3575px; }
  .rail { left: 40px; top: 0; width: 1px; height: 3575px; background: #e6e6e6; }
  .dots { left: 15px; top: 224px; display: flex; flex-direction: column; gap: 15px; }
  .dots span { width: 9px; height: 9px; border-radius: 50%; border: 1px solid #d4d4d4; }
  .dots span.active { background: var(--red); border-color: var(--red); }
  .brand { left: 137px; top: 56px; font-size: 32px; font-weight: 400; color: var(--navy); letter-spacing: .5px; display: flex; align-items: center; gap: 8px; }
  .brand i { width: 9px; height: 9px; background: var(--red); border-radius: 50%; display: inline-block; }
  h1, h2, h3 { color: var(--navy); font-weight: 700; }
  .hero-title { left: 137px; top: 193px; font-size: 30px; line-height: 37px; width: 460px; }
  .hero-sub { left: 137px; top: 274px; font-size: 19px; line-height: 27px; font-weight: 300; color: var(--muted); width: 410px; }
  .field { height: 42px; border-radius: 21px; background: var(--white); border: 1px solid #ececec; font-size: 12px; font-style: italic; font-weight: 300; color: #a8a8a8; padding: 14px 17px; }
  .btn { height: 41px; border-radius: 21px; background: var(--red); color: var(--white); font-size: 15px; display: flex; align-items: center; justify-content: center; }
  .center { text-align: center; }
  .sec-title { font-size: 30px; line-height: 37px; }
  .body-text { font-size: 14.5px; line-height: 21.6px; font-weight: 300; color: var(--text); }
  .label { font-size: 15px; font-weight: 700; color: var(--red); }
  .small-text { font-size: 13px; line-height: 20px; font-weight: 300; }
  .card { width: 292px; height: 274px; background: var(--white); box-shadow: 0 2px 10px rgba(0,0,0,.04); padding: 0 25px; }
  .card .icon { display: block; margin: 20px auto 0; }
  .card h3 { color: var(--red); font-size: 15px; line-height: 18px; margin-top: 14px; }
  .card p { font-size: 12.5px; line-height: 20px; font-weight: 300; margin-top: 15px; }
</style>
</head>
<body>
  <svg class="shapes" viewBox="0 0 1200 3575" aria-hidden="true">
    <polygon points="478,0 750,0 830,460 720,330" fill="#eeeeee"/>
    <path d="M40 648 L210 772 Q260 810 232 862 L40 1193 Z" fill="var(--red)"/>
    <path d="M1200 1366 L1000 1548 Q950 1595 992 1650 L1200 1935 Z" fill="var(--navy)"/>
    <path d="M40 2425 L185 2555 Q232 2600 200 2655 L40 2900 Z" fill="var(--red)"/>
    <path d="M185 2990 L1200 3030 L1200 3575 L740 3575 Q300 3460 150 3415 Q122 3405 122 3370 L122 3055 Q122 2990 185 2990 Z" fill="var(--panel)"/>
  </svg>
  <svg class="abs" style="left:740px;top:0" width="460" height="465" viewBox="0 0 460 465" role="img" aria-label="Portraitfoto des Teams im hellen Büro">
    <defs><linearGradient id="photo" x1="0" y1="0" x2="1" y2="1"><stop offset="0" stop-color="#d9dde0"/><stop offset="1" stop-color="#a9a49b"/></linearGradient></defs>
    <path d="M10 0 L460 0 L460 265 L250 440 Q225 462 195 462 L110 462 Q80 462 75 430 Z" fill="url(#photo)"/>
  </svg>

  <div class="abs rail"></div>
  <div class="abs dots"><span class="active"></span><span></span><span></span><span></span><span></span><span></span><span></span></div>

  <div class="abs brand">Vexalin<i></i></div>
  <h1 class="abs hero-title">Bereit für das nächste Element der Suchmaschinenoptimierung?</h1>
  <p class="abs hero-sub">Vexalin ist Ihre SEO-Agentur für mehr Sichtbarkeit, mehr Reichweite und mehr Traffic</p>
  <div class="abs field" style="left:137px;top:355px;width:233px">Vor- und Nachname</div>
  <div class="abs field" style="left:379px;top:355px;width:233px">Telefon</div>
  <div class="abs field" style="left:137px;top:413px;width:233px">E-Mail-Adresse</div>
  <div class="abs field" style="left:379px;top:413px;width:233px">Website</div>
  <div class="abs btn" style="left:137px;top:487px;width:329px">Jetzt kostenlose Beratung vereinbaren</div>

  <svg class="abs" style="left:572px;top:612px" width="58" height="58" viewBox="0 0 58 58" aria-hidden="true" fill="none" stroke="var(--red)" stroke-width="2">
    <polygon points="29,12 44,21 44,37 29,46 14,37 14,21"/>
    <line x1="14" y1="21" x2="5" y2="12"/><line x1="44" y1="21" x2="53" y2="12"/><line x1="14" y1="37" x2="5" y2="46"/><line x1="44" y1="37" x2="53" y2="46"/>
    <circle cx="5" cy="12" r="3"/><circle cx="53" cy="12" r="3"/><circle cx="5" cy="46" r="3"/><circle cx="53" cy="46" r="3"/><circle cx="29" cy="29" r="4"/>
  </svg>
  <h2 class="abs sec-title center" style="left:300px;top:713px;width:600px">Abrechnung auf Erfolgsbasis –<br>garantiert!</h2>
  <p class="abs body-text center" style="left:295px;top:803px;width:610px">Wie jetzt? Erst bezahlen, wenn die Optimierung erfolgreich war? Genauso ist es! Als erfahrene SEO Agentur bietet wir unsere Leistungen als eine der wenigen zu 100 Prozent auf Erfolgsbasis an. Das heißt, dass Sie von uns erst dann eine Rechnung erhalten, wenn Ihre Webseite auf der 1. Seite der Suchergebnisse rankt. Durch die präzise Zielvorgabe ist sichergestellt, dass Sie keinerlei Risiko eingehen und wir wie immer unser Bestes geben. Warum wir das machen? Weil wir über Jahre hinweg die perfekte Strategie für ein besseres Ranking erforscht haben und damit bisher noch jeden Kunden nach vorne gebracht haben.</p>

  <div class="abs label" style="left:137px;top:1132px">Was ist SEO?</div>
  <p class="abs small-text" style="left:137px;top:1175px;width:297px">SEO steht für Search Engine Optimization, zu Deutsch Suchmaschinenoptimierung, und ist eine der wichtigsten Disziplinen im Online Marketing. Wer heute Informationen benötigt oder ein Problem lösen will, der konsultiert eine Suchmaschine – allen voran Findora. Doch eins wissen Sie selbst am besten: Kaum jemand schaut sich die Suchergebnisse außerhalb von Seite eins ein. Umso wichtiger ist es, mit seiner Webseite genau hier zu ranken. Das aber wollen viele, deshalb führt für erfolgreiche Webseiten kein Weg an der Suchmaschinenoptimierung vorbei. Wir als SEO Agentur unterstützen Sie dabei, aus den zahlreichen Elementen, die für die Suchmaschinenoptimierung notwendig sind, eine funktionierende Verbindung zu schaffen.</p>
  <div class="abs" role="img" aria-label="Linienillustration mit Laborgeräten und Wissenschaftssymbolen" style="left:465px;top:1165px;width:291px;height:298px;border-radius:50%;background:radial-gradient(circle,#ececec 0%,#f3f3f3 60%,var(--bg) 100%)"></div>
  <div class="abs label" style="left:900px;top:1132px;width:163px;text-align:right">Was bringt SEO?</div>
  <p class="abs small-text" style="left:805px;top:1175px;width:258px;text-align:right">Eine prominente Position in den Suchergebnissen führt zu einer Kettenreaktion, die sich jeder Unternehmer wünscht. Je besser Sichtbarkeit und Reichweite, desto mehr Traffic spült Findora auf Ihre Webseite. Wir als führende SEO Agentur sorgen dafür, dass es sich dabei um qualifizierten Traffic handelt, aus dem auch zahlende Kunden werden. Dadurch steigt nicht nur Ihre Konversionsrate, sondern natürlich auch der Umsatz Ihres Unternehmens. Suchmaschinenoptimierung macht sich also bezahlt!</p>

  <h2 class="abs" style="left:137px;top:1594px;font-size:30px">Warum wir?</h2>
  <p class="abs" style="left:137px;top:1637px;font-size:19px;font-weight:300;color:var(--muted)">SEO Agentur mit Herz, Verstand und ganz viel Erfahrung</p>
  <p class="abs body-text" style="left:137px;top:1687px;width:690px">Seit über zehn Jahren forschen wir schwerpunktmäßig an der perfekten Zusammensetzung effektiver Suchmaschinenoptimierung. Als reine SEO Agentur haben wir uns ganz bewusst dafür entschieden, nicht die gesamte Palette des Online Marketings anzubieten, sondern das, wofür unser Herz schlägt und das, was den größten und vor allem nachhaltigsten Erfolg verspricht. Seitdem ist SEO mehr als unser Forschungsgebiet. SEO ist unsere Leidenschaft. Und genau die Liebe zu dem, was wir tun, macht uns so gut, dass wir ausschließlich auf Erfolgsbasis arbeiten.</p>

  <div class="abs card" style="left:137px;top:1911px">
    <svg class="icon" width="40" height="40" viewBox="0 0 40 40" fill="none" stroke="var(--navy)" stroke-width="2"><rect x="4" y="12" width="32" height="24"/><line x1="12" y1="4" x2="12" y2="30"/><line x1="20" y1="4" x2="20" y2="30"/><line x1="28" y1="4" x2="28" y2="30"/></svg>
    <h3>SEO für Anwälte und Steuerberater</h3>
    <p>Große Rechtanwalts- und Steuerberaterkanzleien dominieren den Markt. Mit SEO können sich auch kleine und regionale Anwälte, Notare, Steuer- und Unternehmensberater durchsetzen. Wir helfen Ihnen, sich online als Experte zu profilieren.</p>
  </div>
  <div class="abs card" style="left:454px;top:1911px">
    <svg class="icon" width="40" height="40" viewBox="0 0 40 40" fill="none" stroke="var(--navy)" stroke-width="2"><rect x="15" y="3" width="8" height="18"/><path d="M10 36 H32 M14 36 Q8 28 16 22"/><circle cx="24" cy="27" r="4"/></svg>
    <h3>SEO für Ärzte und Apotheker</h3>
    <p>Ärzte und Apotheker können mit einer suchmaschinen-optimierten Webseite nicht nur neue Patienten und Kunden gewinnen, sondern diesen auch langfristig binden und ihnen zeitgemäße Serviceleistungen anbieten.</p>
  </div>
  <div class="abs card" style="left:770px;top:1911px">
    <svg class="icon" width="40" height="40" viewBox="0 0 40 40" fill="none" stroke="var(--navy)" stroke-width="2"><circle cx="15" cy="15" r="10"/><line x1="22" y1="22" x2="36" y2="36"/></svg>
    <h3>SEO für (Online-)Händler</h3>
    <p>Der Online-Handel boomt, entsprechend groß ist auch die Konkurrenz. Ein Online-Shop ist noch lange kein Selbstläufer und bedarf besonderen Know-hows bei der Suchmaschinen-optimierung. Wir steigern Ihre Verkaufszahlen nachhaltig!</p>
  </div>
  <div class="abs card" style="left:137px;top:2205px">
    <svg class="icon" width="40" height="40" viewBox="0 0 40 40" fill="none" stroke="var(--navy)" stroke-width="2"><polygon points="20,12 28,17 28,26 20,31 12,26 12,17"/><line x1="12" y1="17" x2="5" y2="10"/><line x1="28" y1="17" x2="35" y2="10"/><line x1="20" y1="31" x2="20" y2="38"/></svg>
    <h3>SEO für Handwerker und Dienstleister</h3>
    <p>Wer einen Handwerker oder Dienstleister sucht, der schaut nicht mehr ins Telvora-Verzeichnis, sondern sucht online. Ohne sichtbare Webseite sind Sie für den Kunden quasi nicht existent. Mit Local SEO lässt sich das bereits mit einfachen Mitteln und für kleines Geld ändern!</p>
  </div>
  <div class="abs card" style="left:454px;top:2205px">
    <svg class="icon" width="40" height="40" viewBox="0 0 40 40" fill="none" stroke="var(--navy)" stroke-width="2"><path d="M16 4 H24 M17 4 V14 Q6 20 8 30 Q10 37 20 37 Q30 37 32 30 Q34 20 23 14 V4"/><line x1="9" y1="26" x2="31" y2="26"/></svg>
    <h3>SEO für Online-Portale</h3>
    <p>Online-Portale sind von den Suchmaschinen so abhängig wie kaum ein anderes Internetangebot. Nur wer bei Findora ganz oben steht, erhält ausreichend Traffic um zu überleben. Wir sichern die Zukunft Ihres Portals und bringen Sie in die schwarzen Zahlen.</p>
  </div>
  <div class="abs card" style="left:770px;top:2205px">
    <svg class="icon" width="40" height="40" viewBox="0 0 40 40" fill="none" stroke="var(--navy)" stroke-width="2"><polygon points="20,10 29,15 29,25 20,30 11,25 11,15"/><line x1="11" y1="15" x2="4" y2="8"/><line x1="29" y1="15" x2="36" y2="8"/><line x1="11" y1="25" x2="4" y2="32"/><line x1="29" y1="25" x2="36" y2="32"/><circle cx="4" cy="8" r="2"/><circle cx="36" cy="8" r="2"/><circle cx="4" cy="32" r="2"/><circle cx="36" cy="32" r="2"/></svg>
    <h3>SEO für Sie</h3>
    <p>Es gibt keine Branche, die heutzutage ohne Suchmaschinenoptimierung auskommt. Mit zielgerichteten Maßnahmen setzen wir auch Ihr Business auf ein neues Level, ganz egal wie groß Ihr Unternehmen ist. Sprechen Sie uns noch heute an!</p>
  </div>

  <svg class="abs" style="left:571px;top:2604px" width="58" height="58" viewBox="0 0 58 58" aria-hidden="true" fill="none" stroke="var(--red)" stroke-width="2">
    <polygon points="29,14 42,21 42,37 29,44 16,37 16,21"/>
    <line x1="29" y1="14" x2="29" y2="4"/><line x1="29" y1="44" x2="29" y2="54"/><line x1="16" y1="21" x2="6" y2="15"/><line x1="42" y1="21" x2="52" y2="15"/><line x1="16" y1="37" x2="6" y2="43"/><line x1="42" y1="37" x2="52" y2="43"/>
    <circle cx="29" cy="4" r="2.5"/><circle cx="29" cy="54" r="2.5"/><circle cx="6" cy="15" r="2.5"/><circle cx="52" cy="15" r="2.5"/><circle cx="6" cy="43" r="2.5"/><circle cx="52" cy="43" r="2.5"/>
  </svg>
  <h2 class="abs sec-title center" style="left:300px;top:2682px;width:600px">Lassen Sie sich beraten.<br>Kostenlos und unverbindlich.</h2>
  <p class="abs body-text center" style="left:292px;top:2781px;width:616px">Seit über zehn Jahren forschen wir schwerpunktmäßig an der perfekten Zusammensetzung effektiver Suchmaschinenoptimierung. Als reine SEO Agentur haben wir uns ganz bewusst dafür entschieden, nicht die gesamte Palette des Online Marketings anzubieten, sondern das, wofür unser Herz schlägt und das, was den größten und vor allem nachhaltigsten Erfolg verspricht. Seitdem ist SEO mehr als unser Forschungsgebiet. SEO ist unsere Leidenschaft. Und genau die Liebe zu dem, was wir tun, macht uns so gut, dass wir ausschließlich auf Erfolgsbasis arbeiten.</p>

  <h2 class="abs sec-title center" style="left:250px;top:3093px;width:700px">Jetzt unverbindliche Beratung für Ihe Suchmaschinenoptimierung anfordern</h2>
  <div class="abs field" style="left:216px;top:3225px;width:371px">Vor- und Nachname</div>
  <div class="abs field" style="left:612px;top:3225px;width:371px">Telefonnummer</div>
  <div class="abs field" style="left:216px;top:3291px;width:371px">E-Mail-Adresse</div>
  <div class="abs field" style="left:612px;top:3291px;width:371px">Website</div>
  <div class="abs btn" style="left:513px;top:3394px;width:174px">Anfrage senden</div>
</body>
</html>
```